Graphics for FABRIX NORTH 2014

We need to create 3 product introduction displays for semiconductor trade show. It includes company logo on top, product name and application, product picture, and 2-3 bullet points to describe product features. Attached please find my image.
Required format is higher than 300 dpi at a size of 8 x 10" (vertically long) and file type should be EPS, TIF, or JPG in order of preference.
I need 3 graphics, one per product.

Reason: I need to see more to pick up the most suitable one.

Target Market(s)

High-tech semiconductor manufacturing companies such like Varso, QRT.

Industry/Entity Type

Trade

Font styles to use
Serif

Colors

Designer to choose colors to be used in the design.

Requirements
Must have
• 3 pages, one per product with same format/background
Should not have
• should not have any fancy cartoons. Must be proffesional style.

```html
<!DOCTYPE html>
<html lang="en">
<head>
<meta charset="utf-8">
<title>KALTRON-H3PO4 Reclaim System – Product Display</title>
<link rel="stylesheet" href="https://fonts.googleapis.com/css2?family=Arvo:wght@700&family=Didact+Gothic&family=Open+Sans:wght@400&display=swap">
<style>
  :root {
    --stage: #ffffff;
    --panel: #232323;
    --header: #0b0b0b;
    --header-dot: #1c1c1c;
    --text-light: #f4f4f4;
    --title-ink: #f1ecdc;
    --title-shade: #6d6a60;
    --accent-teal: #a8e4df;
    --bullet-teal: #27c0b5;
    --photo-top: #2463b3;
    --photo-bottom: #4f8bcc;
  }
  * { margin: 0; padding: 0; box-sizing: border-box; }
  html, body {
    width: 1200px; height: 817px; overflow: hidden;
    background: var(--stage);
  }
  .display {
    position: absolute; left: 310px; top: 46px;
    width: 580px; height: 725px;
    border: 1px solid #000;
    overflow: hidden;
  }
  .display-shapes { position: absolute; inset: 0; }
  .company-header {
    position: absolute; left: 0; top: 0; width: 308px; height: 84px;
    display: flex; flex-direction: column; align-items: center; justify-content: center;
    font-family: "Open Sans", sans-serif; font-weight: 400;
    font-size: 19px; line-height: 35px;
    color: var(--text-light);
  }
  .product-name {
    position: absolute; left: 14px; top: 152px; width: 280px;
    font-family: "Arvo", serif; font-weight: 700;
    font-size: 26px; line-height: 33px; letter-spacing: -0.5px;
    color: var(--title-ink);
    text-shadow: 1px 2px 0 var(--title-shade), 2px 3px 0 var(--title-shade);
    transform: rotate(-7deg);
    transform-origin: left top;
  }
  .features-heading {
    position: absolute; left: 26px; top: 282px;
    font-family: "Open Sans", sans-serif; font-weight: 400; font-size: 28px;
    color: var(--accent-teal);
    letter-spacing: 0.5px;
    white-space: nowrap;
  }
  .feature-list {
    position: absolute; left: 43px; top: 370px; width: 215px;
    list-style: none;
    font-family: "Didact Gothic", sans-serif; font-size: 17px; line-height: 20px;
    color: var(--text-light);
  }
  .feature-list li {
    position: relative; padding-left: 13px; margin-bottom: 37px;
  }
  .feature-list li::before {
    content: "\2756"; position: absolute; left: -1px; top: 0;
    font-size: 12px; color: var(--bullet-teal);
  }
</style>
</head>
<body>
  <section class="display">
    <svg class="display-shapes" width="580" height="725" viewBox="0 0 580 725">
      <defs>
        <linearGradient id="photo-tones" x1="0" y1="0" x2="0" y2="1">
          <stop offset="0" stop-color="var(--photo-top)"/>
          <stop offset="1" stop-color="var(--photo-bottom)"/>
        </linearGradient>
        <pattern id="header-dots" width="4" height="4" patternUnits="userSpaceOnUse">
          <rect width="4" height="4" fill="var(--header)"/>
          <rect width="1" height="1" fill="var(--header-dot)"/>
        </pattern>
      </defs>
      <rect class="product-photo" x="280" y="0" width="300" height="725"
            fill="url(#photo-tones)" role="img"
            aria-label="Product photo area: palm-lined city street under a clear blue sky"/>
      <polygon class="side-panel" fill="var(--panel)"
               points="0,0 308,0 308,202 290,231 308,267 308,725 0,725"/>
      <rect class="header-band" x="0" y="0" width="308" height="84" fill="url(#header-dots)"/>
    </svg>

    <header class="company-header">
      <span>Norvelle Technology Inc.</span>
      <span>Logo &amp; Name</span>
    </header>

    <h1 class="product-name">KALTRON-H3PO4<br>Reclaim System</h1>

    <h2 class="features-heading">Product Features:</h2>

    <ul class="feature-list">
      <li>Lorem ipsum dolor sit amet, consectetur adipiscing elit.</li>
      <li>Maecenas tempus lorem quis sapien commodo, quis fermentum metus fringilla.</li>
      <li>Etiam egestas tellus ut nunc congue, vitae tristique lacus aliquam.</li>
    </ul>
  </section>
</body>
</html>
```